Modern book cover design

We are looking for a modern, powerful book cover for a general intrest book about how robots are going to take human jobs in the future.

The book title is "Gearfallow"

It also has a strap line "The end of human jobs and how robots will replace them"
Both the title and the strap line should be on the front cover

I have attached a number of book designs I like, and my author picture.

Reason: Some great submissions but none quite have that wow factor

Target Market(s)

This is a general intrest book, but the reader is likely to be male 30-50

Requirements
Must have
• -Title "Gearfallow"

-Strap-line "The end of human jobs and how robots will replace them"

-Be compliant with PressLoom Cover Design Criteria(www.pressloom-sample.com)

-Book size : 5.5 x 8.5 inches

-Spine size : 0.625 inches

-Must have one author picture on the back cover(attached)

-Must have the following author description on back cover:
"Tom Hardle is a leading futurologist, technologist, inventor, and entrepreneur. With over twenty years of experience in technology and innovation, Tom has travelled the world seeking out and developing new technologies. As a leading voice on the challenges and benefits of tomorrow’s technology, he has advised some of the world’s leading institutions, including the Granite Hall, regarding technological preparations for the future. He is the recipient of the harvest founder of the season prize and has appeared on numerous technology and philanthropy television programs, as well as presenting Clever Little Sparks on Robotics."

-Must have the following book description on back cover:
“Gearfallow is a look at the rapidly changing face of robotics and how it will revolutionize employment over the next thirty years. Tom Hardle lays out the arguments in favor of and against the mechanization of our society, as well as the advantages and untold risks as we march into this ever-present future.”

-Must have the following quote on the back cover:
"A fascinating look into the future of robotics and their impact on humanity, be prepared to question when robots will replace you - Simon Elstree, Professor of Cybernetics at the University of Marlowe”

-Example barcode

```html
<!DOCTYPE html>
<html lang="en">
<head>
<meta charset="utf-8">
<title>Gearfallow – Cover Spread</title>
<link rel="stylesheet" href="https://fonts.googleapis.com/css2?family=Anton&family=Black+Ops+One&family=Marcellus&family=Tinos:ital,wght@0,400;0,700;1,400;1,700&display=swap">
<style>
  :root {
    --page: #ffffff;
    --cover: #000000;
    --ink: #ffffff;
    --title-top: #ffd21a;
    --title-bottom: #f08a00;
    --wire: #3a5fb0;
    --wire-glow: #a9b9e6;
  }
  * { box-sizing: border-box; margin: 0; padding: 0; }
  html, body { width: 1200px; height: 1000px; overflow: hidden; background: var(--page); }
  .canvas { position: relative; width: 1200px; height: 1000px; background: var(--page); }
  .spread {
    position: absolute; left: 65px; top: 124px; width: 1067px; height: 788px;
    background: var(--cover); overflow: hidden; color: var(--ink);
  }

  .data-field {
    position: absolute; left: 480px; top: 380px; width: 420px; height: 380px;
    background: radial-gradient(ellipse at 50% 50%, rgba(40,70,150,.35), rgba(0,0,0,0) 70%);
  }

  /* Back cover */
  .back { position: absolute; left: 0; top: 0; width: 490px; height: 788px; }
  .back-heading {
    position: absolute; left: 0; width: 500px; text-align: center;
    font-family: "Black Ops One", sans-serif; font-size: 18px; letter-spacing: 3px;
  }
  .back-heading.book { top: 70px; }
  .back-heading.author { top: 303px; }
  .blurb {
    position: absolute; left: 25px; top: 116px; width: 455px; text-align: center;
    font-family: "Tinos", serif; font-size: 15px; line-height: 19px;
  }
  .endorsement {
    position: absolute; left: 27px; top: 237px; width: 460px;
    font-family: "Tinos", serif; font-size: 15px; line-height: 19px; font-style: italic;
  }
  .endorsement .attribution { font-weight: 700; }
  .author-photo {
    position: absolute; left: 27px; top: 337px; width: 113px; height: 162px;
    background: linear-gradient(180deg, #d8d8d8 0%, #8c8c8c 55%, #3a3a3a 100%);
  }
  .author-name-back {
    position: absolute; left: 148px; top: 456px;
    font-family: "Marcellus", serif; font-size: 48px; line-height: 48px; letter-spacing: 1px;
    white-space: nowrap;
  }
  .bio {
    position: absolute; left: 15px; top: 503px; width: 452px;
    font-family: "Tinos", serif; font-size: 15px; line-height: 20.5px; text-align: justify;
  }

  /* Spine */
  .spine {
    position: absolute; left: 497px; top: 0; width: 60px; height: 788px;
    writing-mode: vertical-rl;
  }
  .spine-title {
    position: absolute; left: 30px; top: 18px;
    font-family: "Anton", sans-serif; font-size: 30px; line-height: 30px; letter-spacing: 4px;
    white-space: nowrap;
    color: var(--title-bottom);
    background: linear-gradient(90deg, var(--title-top), var(--title-bottom));
    -webkit-background-clip: text; background-clip: text; -webkit-text-fill-color: transparent;
  }
  .spine-author {
    position: absolute; left: 2px; top: 245px;
    font-family: "Black Ops One", sans-serif; font-size: 27px; line-height: 30px; letter-spacing: 3px;
    white-space: nowrap;
  }
  .spine-strap {
    position: absolute; left: 4px; top: 512px;
    font-family: "Tinos", serif; font-size: 13px; line-height: 14px; text-transform: uppercase;
    white-space: nowrap;
  }

  /* Front cover */
  .front { position: absolute; left: 560px; top: 0; width: 507px; height: 788px; }
  .portrait-field {
    position: absolute; right: 0; top: 270px; width: 285px; height: 518px;
    background: radial-gradient(ellipse at 55% 40%, var(--wire-glow) 0%, var(--wire) 35%, rgba(20,35,80,.6) 60%, rgba(0,0,0,0) 78%);
    opacity: .75;
  }
  .title {
    position: absolute; left: 12px; top: 22px; width: max-content;
    font-family: "Anton", sans-serif; font-size: 148px; line-height: 150px; letter-spacing: 1px;
    font-weight: 400;
    white-space: nowrap; transform-origin: left top; transform: scaleX(.68);
    background: linear-gradient(180deg, var(--title-top) 0%, var(--title-bottom) 100%);
    -webkit-background-clip: text; background-clip: text; -webkit-text-fill-color: transparent;
    color: var(--title-bottom);
  }
  .strap-rule {
    position: absolute; left: 172px; width: 180px; height: 3px; background: var(--ink);
  }
  .strap-rule.top { top: 203px; }
  .strap-rule.bottom { top: 276px; }
  .strapline {
    position: absolute; left: 0; top: 215px; width: 500px; text-align: center;
    font-family: "Tinos", serif; font-size: 24px; line-height: 30px; text-transform: uppercase;
    letter-spacing: .5px;
  }
  .author-name-front {
    position: absolute; left: 92px; top: 694px;
    font-family: "Marcellus", serif; font-size: 52px; line-height: 52px; letter-spacing: 1px;
    white-space: nowrap;
  }
</style>
</head>
<body>
<div class="canvas">
  <section class="spread">
    <div class="data-field" role="img" aria-label="Faint blue digital data pattern in the background"></div>

    <article class="back">
      <h2 class="back-heading book">About the Book</h2>
      <p class="blurb">Gearfallow is a look at the rapidly changing face of robotics and how it will revolutionize employment over the next thirty years. Tom Hardle lays out the arguments in favor of and against the mechanization of our society, as well as the advantages and untold risks as we march into this ever-present future</p>
      <p class="endorsement">A fascinating look into the future of robotics and their impact on humanity, be prepared to question when robots will replace you - <span class="attribution">Simon Elstree, Professor of Cybernetics at the University of Marlowe</span></p>
      <h2 class="back-heading author">About the Author</h2>
      <div class="author-photo" role="img" aria-label="Black and white author portrait"></div>
      <div class="author-name-back">TOM HARDLE</div>
      <p class="bio">is a leading futurologist, technologist, inventor, and entrepreneur. With over twenty years of experience in technology and innovation, Tom has travelled the world seeking out and developing new technologies. As a leading voice on the challenges and benefits of tomorrow’s technology, he has advised some of the world’s leading institutions, including the Granite Hall, regarding technological preparations for the future. He is the recipient of the harvest founder of the season prize and has appeared on numerous technology and philanthropy television programs, as well as presenting Clever Little Sparks on Robotics.</p>
    </article>

    <aside class="spine">
      <span class="spine-title">GEARFALLOW</span>
      <span class="spine-author">TOM HARDLE</span>
      <span class="spine-strap">The end of human jobs and how<br>robots will replace them</span>
    </aside>

    <article class="front">
      <div class="portrait-field" role="img" aria-label="Blue wireframe illustration of a human head"></div>
      <h1 class="title">GEARFALLOW</h1>
      <div class="strap-rule top"></div>
      <p class="strapline">The end of human jobs and how<br>robots will replace them</p>
      <div class="strap-rule bottom"></div>
      <div class="author-name-front">TOM HARDLE</div>
    </article>
  </section>
</div>
</body>
</html>
```